A5 Personal trainer profile for brackmoor wellness

I need a A5 Landscape profile designed for the company I work for. Company name is Brackmoor Wellness. The profile is for personal trainers to let people know:

1. Brief description of themselves
2. Qualifications

A picture will be required on the right hand side of the profile. Brackmoor Wellness colours are green and white.

The Brackmoor Wellness Logo in the boarder of the example included must remain. We are looking for a clinical and professional design.

Industry/Entity Type

Health

```html
<!DOCTYPE html>
<html lang="en">
<head>
<meta charset="utf-8">
<title>Personal Trainer Profile – Brackmoor Wellness</title>
<link rel="stylesheet" href="https://fonts.googleapis.com/css2?family=Cabin:ital,wght@0,400;0,700;1,400&display=swap">
<style>
  :root {
    --navy: #16166a;
    --royal: #2a1fd2;
    --body-ink: #3b2b1c;
    --cyan-light: #f2fefe;
    --cyan: #8ef2f6;
    --band: #b4f3f3;
    --rule: #1d4a48;
    --brand-green: #3aa63a;
    --frame-blue: #2f6de0;
    --frame-pale: #cfe0fb;
    --photo-lime: #e9f57a;
    --photo-green: #a9e23c;
    --page: #ffffff;
  }
  * { margin: 0; padding: 0; box-sizing: border-box; }
  html, body { width: 1200px; height: 839px; overflow: hidden; background: var(--page); }
  .profile {
    position: relative; width: 1200px; height: 839px; overflow: hidden;
    background: var(--page);
    font-family: "Cabin", "Trebuchet MS", sans-serif;
    font-variant: small-caps;
  }
  .header-panel {
    position: absolute; left: 0; top: 0; width: 608px; height: 232px;
    background: linear-gradient(to bottom, var(--cyan-light) 0%, var(--cyan) 100%);
  }
  .role-title {
    position: absolute; left: 153px; top: 50px;
    font-size: 40px; font-weight: 400; color: var(--navy); letter-spacing: 0.5px;
  }
  .trainer-name {
    position: absolute; left: 174px; top: 130px;
    font-size: 50px; font-style: italic; font-weight: 400; color: var(--royal);
    font-variant: normal; letter-spacing: -1px;
  }
  .section-heading {
    position: absolute; left: 130px;
    font-size: 23px; font-weight: 700; color: var(--navy);
  }
  .services { top: 250px; }
  .testimonials { top: 425px; }
  .qualifications { top: 565px; }
  .list {
    position: absolute; list-style: none;
    font-size: 19px; color: var(--body-ink); line-height: 22px;
  }
  .list li::before { content: "•"; margin-right: 8px; }
  .service-list { left: 128px; top: 292px; }
  .qualification-list { left: 117px; top: 611px; line-height: 22.5px; }
  .quote {
    position: absolute; left: 128px; top: 472px; width: 760px;
    font-size: 20px; line-height: 22px; color: var(--body-ink);
  }
  .photo-frame {
    position: absolute; left: 770px; top: 82px; width: 322px; height: 328px;
    background: radial-gradient(circle at center, var(--frame-blue) 55%, var(--frame-pale) 100%);
  }
  .photo {
    position: absolute; left: 13px; top: 13px; width: 296px; height: 303px;
    background: linear-gradient(135deg, var(--photo-lime) 0%, var(--photo-green) 100%);
    border: 1px solid var(--navy);
  }
  .right-rule { position: absolute; left: 1183px; top: 0; width: 2px; height: 815px; background: #9aa; }
  .footer-rule { position: absolute; left: 0; top: 812px; width: 1200px; height: 4px; background: var(--rule); }
  .footer-band { position: absolute; left: 0; top: 816px; width: 1200px; height: 23px; background: var(--band); }
  .brand {
    position: absolute; left: 798px; top: 744px; display: flex; align-items: center; gap: 8px;
    font-variant: normal; font-size: 29px; font-weight: 700; color: var(--brand-green);
  }
  .brand-mark { width: 22px; height: 22px; background: var(--brand-green); }
</style>
</head>
<body>
<main class="profile">
  <div class="header-panel"></div>
  <h1 class="role-title">Personal Trainer</h1>
  <h2 class="trainer-name">DANIEL OSEI</h2>

  <div class="photo-frame">
    <div class="photo" role="img" aria-label="Portrait photo of the trainer smiling in a green polo shirt"></div>
  </div>

  <h3 class="section-heading services">How I can help you?</h3>
  <ul class="list service-list">
    <li>Reduce body fat &nbsp;and increase body definition</li>
    <li>Increase stamina, improve agility and speed</li>
    <li>Increase strength and size</li>
    <li>Plyometric training and conditioning</li>
    <li>Flexibility and core strength</li>
  </ul>

  <h3 class="section-heading testimonials">What my clients say about me?</h3>
  <p class="quote">"With Daniel my training is always challenging and fun. I don’t remember a session to be boring or repetitive. In short time I improved my core strength and flexibility. I can run 10k without stopping. It is amazing improvement. &nbsp;" Laura Penhallow</p>

  <h3 class="section-heading qualifications">Qualifications</h3>
  <ul class="list qualification-list">
    <li>Advanced Circuit Training</li>
    <li>Advanced Diploma in Personal Training - Level 3 FPRS Registered</li>
    <li>Fitness Instructor - Level 2 FPRS Registered</li>
    <li>Also qualified in – Suspension training, Studio Cycling, Sports Nutrition, Weight Management</li>
  </ul>

  <div class="brand"><span class="brand-mark"></span>Brackmoor Wellness</div>

  <div class="right-rule"></div>
  <div class="footer-rule"></div>
  <div class="footer-band"></div>
</main>
</body>
</html>
```